Project Management Book Cover Design Project

The book title is:

The Thoroughly Steady Task Leader

Liam Forsythe, MSc, MBA, PMP

It is a book about professional yet common sense project management principles aimed at beginner to experienced project managers. The book is written in a conversational, informal tone with reference to best practice in project management. It is designed to be used as an accessible desk reference. I am looking for a cover design that is striking, eye catching, and professional. It can have an element of fun and informality to reflect the tone of the contents.

I have attached a copy of the draft manuscript so you can get a feel for what the book is like.

see www.qlvx.org for more about the profession of project management

Target Market(s)

Professional Project Managers of all levels (see www.qlvx.org for further information)

Industry/Entity Type

Management

Requirements
Must have
• Must be suitable for 6" x 9" book size

```html
<!DOCTYPE html>
<html lang="en">
<head>
<meta charset="utf-8">
<title>The Thoroughly Steady Task Leader — Cover</title>
<link rel="stylesheet" href="https://fonts.googleapis.com/css2?family=Fira+Sans:wght@600;700&display=swap">
<style>
  :root {
    --stage: #ececec;
    --cover-navy: #261c78;
    --cover-deep: #1a1458;
    --spine-edge: rgba(150, 140, 230, 0.55);
    --ink-light: #ffffff;
    --glow-magenta: #c23bd8;
    --glow-violet: #7a3ce0;
    --glow-orange: #f0641e;
  }
  * { margin: 0; padding: 0; box-sizing: border-box; }
  html, body {
    width: 1200px;
    height: 900px;
    overflow: hidden;
    background: var(--stage);
  }
  .stage {
    position: relative;
    width: 1200px;
    height: 900px;
  }
  .book-cover {
    position: absolute;
    left: 297px;
    top: 70px;
    width: 606px;
    height: 760px;
    background: var(--cover-navy);
    box-shadow: 10px 12px 14px rgba(0, 0, 0, 0.35);
    overflow: hidden;
    font-family: "Fira Sans", Arial, sans-serif;
    color: var(--ink-light);
  }
  .spine {
    position: absolute;
    left: 0;
    top: 0;
    width: 97px;
    height: 100%;
    background: var(--cover-navy);
    border-right: 2px solid var(--spine-edge);
    z-index: 2;
  }
  .spine-title {
    position: absolute;
    left: 58px;
    top: 190px;
    transform-origin: 0 0;
    transform: rotate(90deg);
    white-space: nowrap;
    font-weight: 700;
    font-size: 18px;
    letter-spacing: 0.2px;
  }
  .cover-art {
    position: absolute;
    left: 97px;
    top: 150px;
    right: 0;
    bottom: 0;
    background:
      radial-gradient(ellipse 30% 40% at 22% 70%, rgba(240, 100, 30, 0.75), transparent 70%),
      radial-gradient(ellipse 45% 55% at 45% 45%, rgba(194, 59, 216, 0.75), transparent 70%),
      radial-gradient(ellipse 40% 40% at 80% 75%, rgba(122, 60, 224, 0.55), transparent 70%),
      linear-gradient(180deg, var(--cover-navy) 0%, var(--cover-deep) 100%);
  }
  .front-title {
    position: absolute;
    right: 30px;
    top: 26px;
    text-align: right;
    font-weight: 700;
    font-size: 51px;
    line-height: 64px;
    text-shadow: 3px 3px 4px rgba(0, 0, 0, 0.55);
    z-index: 2;
  }
  .title-rule {
    position: absolute;
    left: 122px;
    right: 20px;
    top: 238px;
    height: 2px;
    background: linear-gradient(90deg, rgba(255,255,255,0.2), var(--ink-light) 40%, var(--ink-light));
    z-index: 2;
  }
  .author {
    position: absolute;
    right: 30px;
    bottom: 28px;
    font-weight: 600;
    font-size: 14px;
    z-index: 2;
  }
</style>
</head>
<body>
  <main class="stage">
    <section class="book-cover">
      <div class="spine">
        <p class="spine-title">The Thoroughly Steady Task Leader</p>
      </div>
      <div class="cover-art" role="img" aria-label="Abstract glowing light streaks in magenta, violet and orange over translucent squares"></div>
      <h1 class="front-title">The Thoroughly<br>Steady<br>Task Leader</h1>
      <div class="title-rule"></div>
      <p class="author">Liam Forsythe, MSc, MBA, PMP</p>
    </section>
  </main>
</body>
</html>
```